Boutique Sparkling Blanc de Blancs Wine label

We are looking for a label and neck label for our new Sparkling Chardonnay.
Images uploaded include, bubbles and glitter maybe as a faded background for whole label?
We like Refined, elegant yet simple designs.
Have included our current table chardonnay label as example.

Industry/Entity Type

Boutique

Font styles to use
Decorative
Script

Requirements
Must have
• Name - "Every Moonlit Hour"
• Methode Traditionelle
• Blanc de Blancs
• 2015
• Beyond the Orchards (Brand)
• Adelaide Hills
Nice to have
• Neutral tones
• Sparkles, Glitter, Bubbles
• Traditional, cursive or vine like fonts
• Have attached fonts we used for previous wine label - might be nice to carry through same/similar fonts to continue our brand?
Should not have
• a lot of colour

```html
<!DOCTYPE html>
<html lang="en">
<head>
<meta charset="utf-8">
<title>Every Moonlit Hour – Sparkling Label Concepts</title>
<link rel="stylesheet" href="https://fonts.googleapis.com/css2?family=Great+Vibes&family=Cinzel:wght@400&display=swap">
<style>
  :root {
    --page: #ffffff;
    --gold-light: #fff6dc;
    --gold-mid: #d9b57e;
    --gold-deep: #a57f4e;
    --bronze: #5e4427;
    --seal: rgba(96, 96, 96, 0.93);
    --cream: #fbf3e6;
    --ink: #0d0b09;
    --shadow: rgba(0, 0, 0, 0.45);
  }
  * { margin: 0; padding: 0; box-sizing: border-box; }
  html, body {
    width: 1200px;
    height: 1000px;
    overflow: hidden;
    background: var(--page);
  }
  .board {
    position: relative;
    width: 1200px;
    height: 1000px;
  }
  .label {
    position: absolute;
    top: 133px;
    width: 586px;
    height: 668px;
    border: 1px solid #3a2b1a;
    box-shadow: 5px 5px 4px var(--shadow);
    overflow: hidden;
  }
  .label--seal { left: 10px; }
  .label--open { left: 607px; }
  .label__backdrop {
    position: absolute;
    inset: 0;
    background:
      radial-gradient(ellipse 45% 22% at 50% 0%, var(--gold-light) 0%, rgba(255, 246, 220, 0.6) 45%, rgba(255, 246, 220, 0) 100%),
      radial-gradient(ellipse 90% 70% at 50% 20%, rgba(240, 214, 168, 0.9) 0%, rgba(217, 181, 126, 0) 80%),
      linear-gradient(180deg, var(--gold-mid) 0%, #c9a16b 55%, var(--gold-deep) 85%, var(--bronze) 100%);
  }
  .seal {
    position: absolute;
    left: 115px;
    top: 131px;
    width: 354px;
    height: 354px;
    border-radius: 50%;
    background: var(--seal);
  }
  .wine-name {
    position: absolute;
    left: 0;
    width: 100%;
    text-align: center;
    font-family: "Great Vibes", cursive;
    font-weight: 400;
    line-height: 1;
  }
  .wine-name__line { display: block; }
  .label--seal .wine-name { top: 205px; color: var(--cream); font-size: 64px; }
  .label--seal .wine-name__line + .wine-name__line { margin-top: 26px; }
  .label--open .wine-name { top: 205px; color: var(--ink); font-size: 64px; }
  .label--open .wine-name__line + .wine-name__line { margin-top: 26px; }
  .vintage {
    position: absolute;
    font-family: "Great Vibes", cursive;
    color: var(--cream);
    font-size: 46px;
    line-height: 1;
  }
  .label--seal .vintage { left: 0; width: 100%; text-align: center; top: 412px; }
  .label--open .vintage { right: 22px; top: 610px; }
  .details {
    position: absolute;
    left: 0;
    width: 100%;
    text-align: center;
    font-family: "Cinzel", serif;
    color: var(--cream);
    line-height: 1;
  }
  .details--style { top: 510px; font-size: 23px; }
  .details--style span { display: block; margin-bottom: 8px; }
  .details--house { top: 602px; }
  .details__brand { display: block; font-size: 23px; margin-bottom: 6px; }
  .details__region { display: block; font-size: 17px; }
</style>
</head>
<body>
<main class="board">

  <section class="label label--seal">
    <div class="label__backdrop" role="img" aria-label="Soft golden glow with glittering sparkles and bokeh bubbles"></div>
    <div class="seal"></div>
    <h1 class="wine-name">
      <span class="wine-name__line">Every Moonlit</span>
      <span class="wine-name__line">Hour</span>
    </h1>
    <p class="vintage">2016</p>
    <p class="details details--style">
      <span>Methode Traditionelle</span>
      <span>Blanc de Blancs</span>
    </p>
    <p class="details details--house">
      <span class="details__brand">Beyond the Orchards</span>
      <span class="details__region">Adelaide Hills</span>
    </p>
  </section>

  <section class="label label--open">
    <div class="label__backdrop" role="img" aria-label="Soft golden glow with glittering sparkles and bokeh bubbles"></div>
    <h1 class="wine-name">
      <span class="wine-name__line">Every Moonlit</span>
      <span class="wine-name__line">Hour</span>
    </h1>
    <p class="details details--style">
      <span>Methode Traditionelle</span>
      <span>Blanc de Blancs</span>
    </p>
    <p class="details details--house">
      <span class="details__brand">Beyond the Orchards</span>
      <span class="details__region">Adelaide Hills</span>
    </p>
    <p class="vintage">2016</p>
  </section>

</main>
</body>
</html>
```